High end Electrical/home automation Business Card

Need a card for a high end electrical and home automation company utilising the existing logo.
Phone
Email
Website

Like black look with raised detail. Don’t necessarily need to keep colour of logo it could be made grayscale or white etc

Target Market(s)

High end clients

Contact Information for Business Card

Ridgeline Electrical

Requirements
Must have
• Logo, phone, email, website, address

High end look
Nice to have
• Black background card
Raised font
Should not have
• Lots of colour

```html
<!DOCTYPE html>
<html lang="en">
<head>
<meta charset="utf-8">
<title>Ridgeline Electrical – Business Card</title>
<link rel="stylesheet" href="https://fonts.googleapis.com/css2?family=Roboto:wght@400;700&display=swap">
<style>
  :root {
    --backdrop: #2b2b2c;
    --card: #1f1f20;
    --card-edge: #2e2e30;
    --ink-light: #f2f2f2;
    --ink-muted: #c9c9c9;
    --accent: #2b93d6;
    --emboss: #3a3a3c;
  }
  html, body {
    margin: 0;
    width: 902px;
    height: 1200px;
    overflow: hidden;
    background: var(--backdrop);
    font-family: "Roboto", Arial, sans-serif;
  }
  .sheet {
    position: relative;
    width: 902px;
    height: 1200px;
  }
  .card {
    position: absolute;
    left: 131px;
    width: 640px;
    height: 366px;
    background: var(--card);
    border: 1px solid var(--card-edge);
    border-radius: 4px;
    box-shadow: 0 18px 40px rgba(0,0,0,.45);
    overflow: hidden;
  }
  .card--front { top: 117px; }
  .card--back  { top: 717px; }

  /* Front */
  .front-name {
    position: absolute;
    left: 44px;
    top: 66px;
    margin: 0;
    font-size: 27px;
    font-weight: 700;
    color: var(--ink-light);
    letter-spacing: .2px;
  }
  .front-mark {
    position: absolute;
    right: 70px;
    top: 60px;
    width: 180px;
    height: 180px;
    border: 14px solid var(--accent);
    border-radius: 50%;
    box-sizing: border-box;
  }
  .address {
    position: absolute;
    left: 44px;
    top: 196px;
    margin: 0;
    font-style: normal;
    font-size: 12.5px;
    line-height: 18px;
    color: var(--ink-muted);
  }
  .contacts {
    position: absolute;
    left: 44px;
    top: 266px;
    margin: 0;
    padding: 0;
    list-style: none;
    font-size: 12.5px;
    line-height: 19px;
    color: var(--ink-muted);
  }
  .contacts li {
    display: flex;
    align-items: center;
    gap: 8px;
  }
  .contacts svg {
    width: 10px;
    height: 10px;
    fill: var(--accent);
    flex: none;
  }

  /* Back */
  .back-emboss {
    position: absolute;
    left: 40px;
    top: 196px;
    margin: 0;
    font-size: 34px;
    font-weight: 700;
    color: var(--emboss);
    text-shadow: 0 1px 0 rgba(255,255,255,.06);
  }
  .back-lockup {
    position: absolute;
    right: 44px;
    top: 120px;
    display: flex;
    align-items: center;
    gap: 12px;
  }
  .back-dot {
    width: 34px;
    height: 34px;
    border-radius: 50%;
    background: var(--accent);
  }
  .back-name {
    margin: 0;
    font-size: 26px;
    font-weight: 700;
    color: var(--ink-light);
  }
</style>
</head>
<body>
<main class="sheet">
  <section class="card card--front" aria-label="Card front">
    <h1 class="front-name">Ridgeline Electrical</h1>
    <div class="front-mark" aria-hidden="true"></div>
    <address class="address">
      118 Larkspur Street<br>
      Suite 210, Fairhaven<br>
      MI 49612
    </address>
    <ul class="contacts">
      <li>
        <svg viewBox="0 0 10 10" aria-hidden="true"><path d="M2 0.5l1.6 2.2-1 1c.6 1.3 1.5 2.2 2.8 2.8l1-1L9.5 7 8.5 9.5C4 9 1 6 .5 1.5z"/></svg>
        555-014-3920
      </li>
      <li>
        <svg viewBox="0 0 10 10" aria-hidden="true"><path d="M0 2h10v6H0z M0 2l5 3.5L10 2" stroke="#1f1f20" stroke-width=".8"/></svg>
        info@ridgelineelectrical.com
      </li>
      <li>
        <svg viewBox="0 0 10 10" aria-hidden="true"><circle cx="5" cy="5" r="4.5"/></svg>
        www.ridgelineelectrical.com
      </li>
    </ul>
  </section>

  <section class="card card--back" aria-label="Card back">
    <p class="back-emboss" aria-hidden="true">Ridgeline Electrical</p>
    <div class="back-lockup">
      <span class="back-dot" aria-hidden="true"></span>
      <h2 class="back-name">Ridgeline Electrical</h2>
    </div>
  </section>
</main>
</body>
</html>
```